Membership Drive "End of Spring Sale"

Looking to run a Direct Debit Sale for November 2019 to boost membership number up. This is our slowest area for membership growth, many choose not to do direct debit, special is designed to increase numbers. Artwork will be display via social media (FB and Instagram) as well as in store. Artwork must be eye catching and direct to the customer. Customer should feel a sense of relief with monthly payments instead of one large payment.

Heading: "End of Spring Special"
Direct Debit
$39.95 per month
Terms and conditions apply"
*Offer End 30th November

Slogan:
"More Energy
More Atmosphere
Feel the Difference
Make the change now" can be placed where suits.

below are other promos we had designed on Artwork Bazaar along with potential photos to be included into this promo

Target Market(s)

Males and Females aged between 18 - 40

Industry/Entity Type

Fitness

Colors

Designer to choose colors to be used in the design.

Requirements
Must have
• Must emphasize "End of Spring Special" $39.95 per month and
• under neath strict terms and conditions apply
• Offer Ends 30th of November
• "All of our contact details"
• Address: 14 Brindle Rd Oakmere 3057
• Ph: 9418 2067
• www.pulsarfit.com.au
• Design format must come in poster size A0 size, Instagram format, Facebook cover and 800 x 800 for the website
Nice to have
• With the photos attached at least one female and one male in the overall design. Lots of color in relation to Spring and artistic effects to catch peoples eyes.
• Also to include "Celebrating 49 years"

```html
<!DOCTYPE html>
<html lang="en">
<head>
<meta charset="utf-8">
<title>End of Spring Special – Pulsar Fitness social set</title>
<link href="https://fonts.googleapis.com/css2?family=Anton&family=Saira+Semi+Condensed:wght@400;600;800&display=swap" rel="stylesheet">
<style>
:root{
  --board:#4d4d4d;
  --yellow:#f2c94c;
  --label:#f4c542;
  --ink:#161616;
  --white:#ffffff;
  --sky:#c9ebf7;
  --paper:#fbf9f1;
  --skin-a:#c98a5e;
  --skin-b:#7a4a2e;
}
*{margin:0;padding:0;box-sizing:border-box}
html,body{width:1200px;height:784px;overflow:hidden;background:var(--board)}
body{position:relative;font-family:"Saira Semi Condensed",sans-serif}

.board-label{position:absolute;font-weight:800;font-size:21px;color:var(--label);letter-spacing:.2px}
.label-facebook{left:113px;top:72px}
.label-instagram{left:561px;top:72px}
.label-web{left:124px;top:706px}

.ad{position:absolute;overflow:hidden;box-shadow:0 4px 14px rgba(0,0,0,.45);
  background:linear-gradient(170deg,var(--sky) 0%,#eaf7fb 40%,var(--paper) 70%,#fdf3cf 100%)}
.ad svg.bands{position:absolute;inset:0;width:100%;height:100%}
.athlete-photo{position:absolute;
  background:radial-gradient(ellipse at 50% 35%,var(--skin-a) 0%,var(--skin-b) 60%,rgba(60,40,30,0) 78%)}

/* headline: one rotated group, lines placed in its own axis */
.headline-group{position:absolute;left:72px;top:14px;width:0;height:0;transform:rotate(35deg);transform-origin:left top}
.headline{position:absolute;font-family:"Anton",sans-serif;line-height:.85;white-space:nowrap;transform-origin:left top}
.hl-endof{left:0;top:22px;font-size:24px;line-height:.95;color:var(--ink);writing-mode:vertical-rl;transform:rotate(180deg);transform-origin:center}
.hl-spring{left:50px;top:0;font-size:96px;color:var(--ink);transform:scaleX(.85)}
.hl-special{left:42px;top:86px;font-size:150px;color:var(--white);transform:scaleX(.8)}

.brand-name{position:absolute;font-family:"Anton",sans-serif;color:var(--ink);letter-spacing:.5px;line-height:1;white-space:nowrap}

.offer{position:absolute}
.offer .kicker{color:var(--yellow);font-weight:600;line-height:1}
.offer .slogan{color:var(--ink);font-weight:600;line-height:1.05}
.offer .tag-row,.offer .pm-row{display:flex;align-items:center}
.offer .tag{background:var(--yellow);color:var(--ink);font-weight:800;line-height:1;clip-path:polygon(0 0,100% 0,92% 100%,0 100%)}
.offer .rule{flex:1;height:1.5px;background:var(--ink)}
.offer .price{font-weight:800;color:var(--ink);line-height:.9;letter-spacing:-1px}
.offer .price sup{font-size:.45em;vertical-align:.9em;margin-right:1px}
.offer .per-month{background:var(--ink);color:var(--yellow);font-weight:800;letter-spacing:1.5px;line-height:1}
.offer .terms{color:var(--ink);white-space:nowrap}
.offer .terms b{font-weight:600}

.contact-bar{position:absolute;left:0;right:0;bottom:0;background:var(--ink);display:flex;align-items:center;justify-content:center;color:var(--yellow);white-space:nowrap}
.contact-bar svg{stroke:var(--white);fill:none}
.contact-bar span{display:inline-flex;align-items:center}

/* square format, built at 522px */
.square{width:522px;height:522px}
.ad-instagram{left:562px;top:114px}
.ad-web-wrap{position:absolute;left:124px;top:310px;width:387px;height:387px}
.ad-web{left:0;top:0;transform:scale(.7414);transform-origin:left top}

.square .athlete-photo{left:262px;top:42px;width:270px;height:446px;border-radius:45% 40% 8% 20%}
.square .brand-name{right:14px;top:20px;font-size:22px}
.square .offer{left:13px;top:333px;width:180px}
.square .kicker{font-size:15px}
.square .slogan{font-size:19px;margin-top:2px}
.square .tag-row{margin-top:4px}
.square .tag{font-size:14px;padding:1px 16px 1px 6px}
.square .price{font-size:56px;margin-top:2px}
.square .per-month{font-size:13px;padding:2px 6px}
.square .terms{font-size:9px;margin-top:6px}
.square .terms .date{font-size:12px;font-weight:600}
.square .contact-bar{height:36px;gap:14px;font-size:14px}
.square .contact-bar svg{width:13px;height:13px;margin-right:6px}

/* facebook cover */
.ad-facebook{left:114px;top:114px;width:397px;height:151px}
.ad-facebook .headline-group{left:43px;top:2px;transform:rotate(35deg) scale(.35)}
.ad-facebook .athlete-photo{left:128px;top:2px;width:112px;height:149px;border-radius:45% 45% 6% 6%}
.ad-facebook .brand-name{left:14px;top:122px;font-size:11px;line-height:.95}
.ad-facebook .offer{left:243px;top:8px;width:120px}
.ad-facebook .kicker{font-size:12px;text-align:center}
.ad-facebook .slogan{font-size:16px;text-align:center}
.ad-facebook .tag-row{margin-top:3px}
.ad-facebook .tag{font-size:10px;padding:1px 10px 1px 4px}
.ad-facebook .price{font-size:36px;margin-top:1px;text-align:center}
.ad-facebook .per-month{font-size:9px;padding:1px 5px}
.ad-facebook .terms{font-size:6px;margin-top:3px;text-align:center}
.ad-facebook .terms .date{font-size:9px;font-weight:600}
.ad-facebook .url-strip{position:absolute;left:200px;right:0;bottom:0;height:14px;background:var(--ink);color:var(--yellow);font-size:7px;letter-spacing:1px;display:flex;align-items:center;justify-content:center}
</style>
</head>
<body>

<div class="board-label label-facebook">FACEBOOK</div>
<div class="board-label label-instagram">INSTAGRAM</div>
<div class="board-label label-web">FOR WEB</div>

<!-- Facebook cover -->
<section class="ad ad-facebook">
  <svg class="bands" viewBox="0 0 397 151" preserveAspectRatio="none" aria-hidden="true">
    <polygon points="0,0 95,0 330,151 184,151 0,22" fill="#f2c94c"/>
    <polygon points="0,22 184,151 101,151 0,80" fill="#161616"/>
    <line x1="0" y1="14" x2="210" y2="125" stroke="#161616" stroke-width="1.2"/>
  </svg>
  <div class="athlete-photo" role="img" aria-label="Muscular male athlete carrying weight plates"></div>
  <div class="headline-group">
    <div class="headline hl-endof">END<br>OF</div>
    <div class="headline hl-spring">SPRING</div>
    <div class="headline hl-special">SPECIAL</div>
  </div>
  <div class="brand-name">PULSAR<br>FITNESS</div>
  <div class="offer">
    <div class="kicker">MAKE THE</div>
    <div class="slogan">CHANGE NOW</div>
    <div class="tag-row"><span class="tag">DIRECT DEBIT</span><span class="rule"></span></div>
    <div class="price"><sup>$</sup>39.95</div>
    <div class="pm-row"><span class="rule"></span><span class="per-month">PER MONTH</span></div>
    <div class="terms">Terms and conditions apply*</div>
    <div class="terms">Offer End <span class="date">30TH NOVEMBER</span></div>
  </div>
  <div class="url-strip">www.pulsarfit.com.au</div>
</section>

<!-- Instagram square -->
<section class="ad square ad-instagram">
  <svg class="bands" viewBox="0 0 522 522" preserveAspectRatio="none" aria-hidden="true">
    <polygon points="0,0 100,0 522,270 522,420 0,104" fill="#f2c94c"/>
    <polygon points="0,104 522,400 522,522 470,522 0,262" fill="#161616"/>
    <line x1="98" y1="14" x2="240" y2="85" stroke="#161616" stroke-width="1.5"/>
  </svg>
  <div class="athlete-photo" role="img" aria-label="Muscular male athlete carrying weight plates"></div>
  <div class="headline-group">
    <div class="headline hl-endof">END<br>OF</div>
    <div class="headline hl-spring">SPRING</div>
    <div class="headline hl-special">SPECIAL</div>
  </div>
  <div class="brand-name">PULSAR FITNESS</div>
  <div class="offer">
    <div class="kicker">MAKE THE</div>
    <div class="slogan">CHANGE NOW</div>
    <div class="tag-row"><span class="tag">DIRECT DEBIT</span><span class="rule"></span></div>
    <div class="price"><sup>$</sup>39.95</div>
    <div class="pm-row"><span class="rule"></span><span class="per-month">PER MONTH</span></div>
    <div class="terms"><b>Terms and conditions apply*</b> &nbsp; Offer End <span class="date">30TH NOVEMBER</span></div>
  </div>
  <div class="contact-bar">
    <span><svg viewBox="0 0 16 16" stroke-width="1.4"><path d="M8 15s-5-5-5-8.5a5 5 0 0 1 10 0C13 10 8 15 8 15z"/><circle cx="8" cy="6.5" r="1.8"/></svg>14 Brindle Rd Oakmere 3057</span>
    <span><svg viewBox="0 0 16 16" stroke-width="1.4"><path d="M3 2h3l1.5 3.5-2 1.2a8 8 0 0 0 3.8 3.8l1.2-2L14 10v3a1 1 0 0 1-1 1A11 11 0 0 1 2 3a1 1 0 0 1 1-1z"/></svg>9418 2067</span>
    <span><svg viewBox="0 0 16 16" stroke-width="1.3"><circle cx="8" cy="8" r="6.5"/><ellipse cx="8" cy="8" rx="2.8" ry="6.5"/><path d="M1.5 8h13"/></svg>www.pulsarfit.com.au</span>
  </div>
</section>

<!-- Web 800x800 -->
<div class="ad-web-wrap">
<section class="ad square ad-web">
  <svg class="bands" viewBox="0 0 522 522" preserveAspectRatio="none" aria-hidden="true">
    <polygon points="0,0 100,0 522,270 522,420 0,104" fill="#f2c94c"/>
    <polygon points="0,104 522,400 522,522 470,522 0,262" fill="#161616"/>
    <line x1="98" y1="14" x2="240" y2="85" stroke="#161616" stroke-width="1.5"/>
  </svg>
  <div class="athlete-photo" role="img" aria-label="Muscular male athlete carrying weight plates"></div>
  <div class="headline-group">
    <div class="headline hl-endof">END<br>OF</div>
    <div class="headline hl-spring">SPRING</div>
    <div class="headline hl-special">SPECIAL</div>
  </div>
  <div class="brand-name">PULSAR FITNESS</div>
  <div class="offer">
    <div class="kicker">MAKE THE</div>
    <div class="slogan">CHANGE NOW</div>
    <div class="tag-row"><span class="tag">DIRECT DEBIT</span><span class="rule"></span></div>
    <div class="price"><sup>$</sup>39.95</div>
    <div class="pm-row"><span class="rule"></span><span class="per-month">PER MONTH</span></div>
    <div class="terms"><b>Terms and conditions apply*</b> &nbsp; Offer End <span class="date">30TH NOVEMBER</span></div>
  </div>
  <div class="contact-bar">
    <span><svg viewBox="0 0 16 16" stroke-width="1.4"><path d="M8 15s-5-5-5-8.5a5 5 0 0 1 10 0C13 10 8 15 8 15z"/><circle cx="8" cy="6.5" r="1.8"/></svg>14 Brindle Rd Oakmere 3057</span>
    <span><svg viewBox="0 0 16 16" stroke-width="1.4"><path d="M3 2h3l1.5 3.5-2 1.2a8 8 0 0 0 3.8 3.8l1.2-2L14 10v3a1 1 0 0 1-1 1A11 11 0 0 1 2 3a1 1 0 0 1 1-1z"/></svg>9418 2067</span>
    <span><svg viewBox="0 0 16 16" stroke-width="1.3"><circle cx="8" cy="8" r="6.5"/><ellipse cx="8" cy="8" rx="2.8" ry="6.5"/><path d="M1.5 8h13"/></svg>www.pulsarfit.com.au</span>
  </div>
</section>
</div>

</body>
</html>
```